Marquise Velora Saddlery Goods - Elite line of horse care grooming products

I wanted to have a label design for my equestrian products that made the people who use them on their horses feel like a princess. I use all natural ingredients, they smell wonderful and work! I think my current design could be more amazing.... I have a total of 6 products. The final design should communicate that you are using the finest and highest quality ingredients on your best friend. please see my website (www.MarquiseSaddlery.example) for the design aesthetic I'm going for. Design Guide:
The design should communicate that you are using the finest and highest quality ingredients on your best friend.
Create a bold, unique, visually-appealing design
Make buyer feel like a princess
Impart that you are taking care of your horse because you’re buying the best
Stand out from most other products currently on the market that look boring/outdated, bland
Avoid any design or visual images that impart chemical, industrial or commercial connotations
Key Terms: Elite, Bold, Serious, Baroque elegance, Feminine, Elegance, Wow, Fairytale, Fantasy, Elegance,

Please create: Design separate front and back BOPP labels for 32oz. spray bottle, 3.5x5” Rosemary, Lavender & Mint Insect Repellent

Design should convey a sense of wealth and prestige
Elegance & sophistication
Professional quality

Design Guide:

Key Attributes of Product:
Expensive product
Therapeutic-grade essential oils
All-natural ingredients
No poisons or pesticides
Smell wonderful
They work

Please use royal purple and gold

Target Market(s)

High end female horse owners..12-65yo female horse owners who want to and can afford to buy premium products for horse grooming.

Font styles to use
Sans Serif
Decorative
Script

Colors
876aae

Requirements
Must have
• Elegance, wow, pick me. Mandatory Graphics:
• Marquise Velora Saddlery Goods logo with gold doily (no gradient on gold)
Nice to have
• Fairytale, fantasy, quality, elite, smells good,
Should not have
• I do not want my bottles to look like pesticides or poison.

```html
<!DOCTYPE html>
<html lang="en">
<head>
<meta charset="utf-8">
<title>Marquise Velora Saddlery Goods – Natural Insect Repellent Label</title>
<link rel="stylesheet" href="https://fonts.googleapis.com/css2?family=Josefin+Sans:wght@300;400&family=Parisienne&display=swap">
<style>
  :root {
    --royal-purple: #4b2a7d;
    --soft-purple: #876aae;
    --lilac: #b59ad3;
    --gold-light: #f3d9a6;
    --gold: #c9a46a;
    --gold-dark: #7a5a3c;
    --paper: #fdfbfd;
    --text: #4a3a5a;
    --lavender: #6b45a8;
    --stem: #8fae6a;
    --ribbon: #c9b6df;
  }
  * { margin: 0; padding: 0; box-sizing: border-box; }
  html, body { width: 840px; height: 1200px; overflow: hidden; }
  body { font-family: "Josefin Sans", sans-serif; background: #fff; }

  .label {
    position: relative;
    width: 840px;
    height: 1200px;
    overflow: hidden;
  }

  .floral-backdrop {
    position: absolute;
    inset: 0;
    background:
      radial-gradient(circle at 6% 32%, #9d72c4 0, rgba(157,114,196,0) 20%),
      radial-gradient(circle at 96% 60%, #7f4fb0 0, rgba(127,79,176,0) 18%),
      radial-gradient(circle at 20% 4%, #e6c8e4 0, rgba(230,200,228,0) 25%),
      radial-gradient(circle at 85% 5%, #d7b3de 0, rgba(215,179,222,0) 22%),
      radial-gradient(circle at 60% 98%, #b98bcf 0, rgba(185,139,207,0) 22%),
      linear-gradient(160deg, #f3e4f2, #e6d2ec 50%, #f2e3f1);
  }

  .card {
    position: absolute;
    left: 64px;
    top: 64px;
    width: 712px;
    height: 1072px;
    padding: 12px;
    background: linear-gradient(135deg, var(--gold-light), var(--gold) 35%, var(--gold-dark) 70%, var(--gold-light));
    box-shadow: 0 6px 18px rgba(60, 30, 70, 0.35);
  }
  .card-inner {
    width: 100%;
    height: 100%;
    background:
      radial-gradient(circle at 70% 40%, rgba(239,225,240,0.55), rgba(255,255,255,0) 45%),
      radial-gradient(circle at 30% 75%, rgba(239,225,240,0.5), rgba(255,255,255,0) 40%),
      var(--paper);
  }

  .doily {
    position: absolute;
    left: 212px;
    top: 124px;
    width: 416px;
    height: 476px;
    border-radius: 50%;
    background: radial-gradient(closest-side, rgba(255,255,255,0) 70%, rgba(243,217,166,0.85) 78%, rgba(201,164,106,0.8) 88%, rgba(122,90,60,0.45) 97%, rgba(255,255,255,0) 100%);
  }

  .brand-name {
    position: absolute;
    left: 232px;
    top: 328px;
    width: 376px;
    text-align: center;
    font-weight: 400;
    font-size: 28px;
    line-height: 1.3;
    color: var(--royal-purple);
  }

  .product-title {
    position: absolute;
    left: 198px;
    top: 676px;
    width: 448px;
    font-weight: 300;
    font-size: 46px;
    letter-spacing: -1.2px;
    color: var(--royal-purple);
    white-space: nowrap;
  }

  .blend-name {
    position: absolute;
    left: 194px;
    top: 772px;
    width: 448px;
    height: 47px;
    border-top: 2px solid var(--lilac);
    border-bottom: 2px solid var(--lilac);
    padding-top: 11px;
    text-align: center;
    font-weight: 300;
    font-size: 23px;
    letter-spacing: 4px;
    color: var(--soft-purple);
    white-space: nowrap;
  }

  .blend-word {
    position: absolute;
    left: 194px;
    top: 829px;
    width: 448px;
    text-align: center;
    font-weight: 300;
    font-size: 21px;
    letter-spacing: 6px;
    color: var(--soft-purple);
  }

  .description {
    position: absolute;
    left: 194px;
    top: 874px;
    width: 444px;
    font-weight: 300;
    font-size: 20.5px;
    line-height: 29px;
    color: var(--text);
  }
  .description .line {
    display: block;
    text-align: justify;
    text-align-last: justify;
    white-space: nowrap;
  }
  .description .line-last { text-align-last: left; }

  .tagline {
    position: absolute;
    left: 290px;
    top: 1020px;
    font-family: "Parisienne", cursive;
    font-size: 44px;
    color: var(--royal-purple);
    transform: rotate(-8deg);
    transform-origin: left center;
    white-space: nowrap;
  }
  .tagline-swash {
    position: absolute;
    left: 384px;
    top: 1074px;
  }

  .lavender-bouquet {
    position: absolute;
    left: 28px;
    top: 530px;
    width: 160px;
    height: 670px;
    border-radius: 80px 80px 0 0;
    background: linear-gradient(180deg,
      var(--lavender) 0%, #7b56b6 34%,
      var(--stem) 50%, #a9c289 62%,
      var(--ribbon) 75%, #ddd0ea 100%);
    opacity: 0.9;
  }
</style>
</head>
<body>
  <main class="label">
    <div class="floral-backdrop" role="img" aria-label="Soft purple watercolour flowers and leaves filling the background"></div>

    <section class="card">
      <div class="card-inner"></div>
    </section>

    <div class="doily" role="img" aria-label="Gold baroque lace doily frame around the brand name"></div>
    <p class="brand-name">Marquise Velora<br>Saddlery Goods</p>

    <div class="lavender-bouquet" role="img" aria-label="Bouquet of lavender sprigs tied with a lilac gingham ribbon"></div>

    <h1 class="product-title">Natural Insect Repellent</h1>
    <p class="blend-name">LAVENDER, MINT &amp; ROSEMARY</p>
    <p class="blend-word">BLEND</p>

    <p class="description">
      <span class="line">Natural ingredients made with therapeutic grade</span>
      <span class="line">essential oils! Free of harsh chemicals, lovely</span>
      <span class="line">smell. Safe for humans too...go ahead, spray it</span>
      <span class="line line-last">on yourself!</span>
    </p>

    <p class="tagline">Love your horse!</p>
    <svg class="tagline-swash" width="66" height="14" viewBox="0 0 66 14" aria-hidden="true">
      <path d="M3 10 Q33 4 63 5" fill="none" stroke="#4b2a7d" stroke-width="4" stroke-linecap="round"/>
    </svg>
  </main>
</body>
</html>
```